Classy, Elegant, Simple Business Card Design

Looking to have a classy, simple, and elegant design. Want a top notch designed business card. I really like the look of the new brivo credit card. I also like the design I attached. I am trying to reach 21-29 year old females for booking us for there wedding or event. We offer Disc Jockey Service, Photo Booth Rentals, and Uplighting .

Target Market(s)

21-28 year old females

Contact Information for Business Card

Has to have logo, website, email, and phone number

Font styles to use
Other font styles liked:
• open to font choice, modern, clean
Designer to choose
33a6d7
0791cd
0555a3
ffffff

Requirements
Must have
• Has to have logo, website, email, and phone number
Nice to have
• I really like the design of the new brivo credit card. I also included my logo and some designs I like
Should not have
• clutter or too much info

```html
<!DOCTYPE html>
<html lang="en">
<head>
<meta charset="utf-8">
<title>Harborline Event Group – Business Card</title>
<link rel="stylesheet" href="https://fonts.googleapis.com/css2?family=Open+Sans:ital,wght@0,400;0,600;0,700;1,600&display=swap">
<style>
  :root {
    --page-bg: #0b1a2e;
    --card-light: #24617f;
    --card-mid: #174a6a;
    --card-dark: #0b2038;
    --sky: #33a6d7;
    --azure: #0791cd;
    --royal: #0555a3;
    --icon-tile: #5ccbea;
    --icon-line: #1d4f6b;
    --white: #ffffff;
  }
  * { box-sizing: border-box; margin: 0; padding: 0; }
  html, body { width: 1200px; height: 1200px; overflow: hidden; }
  body {
    background: var(--page-bg);
    font-family: "Open Sans", Arial, sans-serif;
    color: var(--white);
    position: relative;
  }
  .card {
    position: absolute;
    left: 194px;
    width: 813px;
    height: 464px;
    border-radius: 18px;
    background: linear-gradient(128deg, var(--card-light) 0%, var(--card-mid) 38%, var(--card-dark) 78%);
  }
  .card--front { top: 122px; }
  .card--back { top: 615px; }

  .holder { position: absolute; left: 53px; top: 88px; }
  .holder__name {
    font-size: 27px; font-weight: 700; letter-spacing: 0.5px; line-height: 1;
  }
  .holder__name em { font-weight: 600; font-style: italic; }
  .holder__title {
    margin-top: 4px; margin-left: 2px;
    font-size: 15px; font-weight: 600; letter-spacing: 2.6px;
  }

  .contacts { position: absolute; left: 51px; top: 232px; list-style: none; }
  .contacts__item { display: flex; align-items: center; height: 36px; margin-bottom: 15px; }
  .contacts__icon {
    width: 36px; height: 36px; border-radius: 7px;
    background: var(--icon-tile);
    display: flex; align-items: center; justify-content: center;
    flex-shrink: 0;
  }
  .contacts__icon svg { width: 24px; height: 24px; }
  .contacts__text { margin-left: 19px; font-size: 21px; font-weight: 600; letter-spacing: 0.4px; }

  .front-brand {
    position: absolute; right: 44px; top: 200px;
    font-size: 44px; font-weight: 600; letter-spacing: 2px;
    color: var(--sky);
  }

  .brand {
    position: absolute; left: 0; right: 0; top: 140px;
    display: flex; flex-direction: column; align-items: center;
  }
  .brand__dot {
    width: 64px; height: 64px; border-radius: 50%;
    background: var(--azure);
    margin-bottom: 34px;
  }
  .brand__name {
    font-size: 37px; font-weight: 600; letter-spacing: 1px; line-height: 1;
    color: var(--white);
  }
  .brand__sub {
    margin-top: 10px; padding-left: 10px;
    font-size: 17px; font-weight: 600; letter-spacing: 10px;
    color: var(--white);
  }
</style>
</head>
<body>

  <section class="card card--front" aria-label="Card front">
    <div class="holder">
      <p class="holder__name">DORIAN K. <em>MALLORY</em></p>
      <p class="holder__title">CEO / MANAGER</p>
    </div>

    <ul class="contacts">
      <li class="contacts__item">
        <span class="contacts__icon">
          <svg viewBox="0 0 24 24" fill="none" stroke="var(--icon-line)" stroke-width="1.3" stroke-linecap="round" stroke-linejoin="round" aria-hidden="true">
            <path d="M6.5 3.5l3 3.2-1.8 2.2c1 2.2 3 4.3 5.3 5.4l2.2-1.8 3.2 3-2 2.5C11 17.7 6.3 13 4 7.2z"/>
            <path d="M13.5 6.5a4 4 0 0 1 4 4M13.5 3.5a7 7 0 0 1 7 7"/>
          </svg>
        </span>
        <span class="contacts__text">+1 555 0142 778</span>
      </li>
      <li class="contacts__item">
        <span class="contacts__icon">
          <svg viewBox="0 0 24 24" fill="none" stroke="var(--icon-line)" stroke-width="1.3" aria-hidden="true">
            <circle cx="12" cy="12" r="9"/>
            <ellipse cx="12" cy="12" rx="4" ry="9"/>
            <path d="M3 12h18M4.5 7.5h15M4.5 16.5h15M12 3v18"/>
          </svg>
        </span>
        <span class="contacts__text">www.harborlinevents.com</span>
      </li>
      <li class="contacts__item">
        <span class="contacts__icon">
          <svg viewBox="0 0 24 24" fill="none" stroke="var(--icon-line)" stroke-width="1.3" stroke-linejoin="round" aria-hidden="true">
            <rect x="3" y="6" width="18" height="12" rx="1"/>
            <path d="M3 6.5l9 7 9-7M3 17.5l7-6M21 17.5l-7-6"/>
          </svg>
        </span>
        <span class="contacts__text">hello@harborline.co</span>
      </li>
    </ul>

    <p class="front-brand">HARBORLINE</p>
  </section>

  <section class="card card--back" aria-label="Card back">
    <div class="brand">
      <span class="brand__dot"></span>
      <p class="brand__name">HARBORLINE</p>
      <p class="brand__sub">EVENT GROUP</p>
    </div>
  </section>

</body>
</html>
```